New Web Design Project

See attachments on the content and concept. Very important that the flow of the tiers stand out

Target Market(s)

Food and Beverage Manufacturing

Industry/Entity Type

Food and Beverage

Coding

Coded - Design and coding required

Number of Pages Required

3 page

Colors
0054AA
0677BA
7BADD7
CADEEF
E8F1F8

```html
<!DOCTYPE html>
<html lang="en">
<head>
<meta charset="utf-8">
<title>Northvale Consulting Group — SQF Consulting</title>
<link href="https://fonts.googleapis.com/css2?family=Poppins:wght@400;500;600;700&family=Playfair+Display:ital,wght@0,500;0,600;1,500;1,600&display=swap" rel="stylesheet">
<style>
:root{
  --blue-900:#0054AA;
  --blue-700:#0677BA;
  --blue-400:#7BADD7;
  --blue-200:#CADEEF;
  --blue-50:#E8F1F8;
  --navy:#0c2650;
  --ink:#1a2434;
  --muted:#4a5566;
  --white:#ffffff;
  --sans:'Poppins',sans-serif;
  --serif:'Playfair Display',serif;
}
*{box-sizing:border-box;margin:0;padding:0}
html,body{width:1200px;height:4699px;overflow:hidden}
body{font-family:var(--sans);color:var(--ink);background:var(--white);position:relative}
a{color:inherit;text-decoration:none}
.container{width:920px;margin:0 auto;position:relative}
.accent{font-family:var(--serif);font-style:italic;font-weight:600;color:var(--blue-900)}
.underline{position:relative;display:inline-block}
.underline svg{position:absolute;left:0;bottom:-10px;width:100%;height:12px}
.eyebrow{font-size:12px;font-weight:500;letter-spacing:.5px;color:var(--blue-700);text-transform:uppercase;text-align:center}
.section-title{font-size:30px;font-weight:600;line-height:42px;text-align:center;color:var(--ink);margin-top:10px}
.section-lead{font-size:13px;line-height:22px;text-align:center;color:var(--muted);margin-top:26px}

/* buttons */
.btn{display:inline-flex;align-items:center;gap:14px;height:40px;padding:0 6px 0 20px;border-radius:22px;font-size:12px;font-weight:500;letter-spacing:.3px;text-transform:uppercase}
.btn .dot{width:28px;height:28px;border-radius:50%;display:flex;align-items:center;justify-content:center}
.btn-solid{background:var(--blue-900);color:var(--white)}
.btn-solid .dot{background:var(--white);color:var(--blue-900)}
.btn-outline{border:1.5px solid var(--blue-900);color:var(--blue-900);background:var(--white)}
.btn-outline .dot{background:var(--blue-900);color:var(--white)}
.btn-ghost{border:1.5px solid rgba(255,255,255,.8);color:var(--white)}
.btn-ghost .dot{background:rgba(255,255,255,.15);color:var(--white)}
.btn-plain{padding:0 20px}
.btn-row{display:flex;justify-content:center;gap:16px}

/* top bar */
.topbar{height:33px;background:var(--blue-900);color:var(--white);font-size:12px}
.topbar .container{display:flex;align-items:center;height:33px;gap:28px;width:1096px}
.topbar .item{display:flex;align-items:center;gap:6px}
.topbar .item.phone{font-weight:600;letter-spacing:.5px}
.socials{margin-left:auto;display:flex;gap:12px}
.socials span{width:11px;height:11px;border-radius:50%;background:var(--white);display:block}

/* header */
.site-header{height:77px;background:var(--white)}
.site-header .container{width:1096px;display:flex;align-items:center;height:77px}
.brand{display:flex;align-items:center;gap:12px}
.brand-mark{width:44px;height:44px;border-radius:50%;border:2.5px solid var(--blue-900)}
.brand-name{font-family:var(--serif);font-size:22px;font-weight:500;color:var(--navy);line-height:24px}
.brand-tag{font-size:10px;letter-spacing:1px;color:var(--blue-900);margin-top:3px}
.nav{display:flex;gap:42px;margin-left:78px;font-size:12px;font-weight:500;color:var(--ink)}
.nav .active{color:var(--blue-900)}
.site-header .btn{margin-left:auto}

/* hero */
.hero{height:543px;position:relative;overflow:hidden}
.hero-photo{position:absolute;inset:0;background:linear-gradient(90deg,#1e3550 0%,#4a6077 40%,#9fb2c2 70%,#c9d6df 100%)}
.hero-shade{position:absolute;inset:0;background:linear-gradient(90deg,rgba(10,24,44,.85) 0%,rgba(10,24,44,.55) 45%,rgba(10,24,44,0) 70%)}
.hero-content{position:absolute;left:106px;top:100px;width:460px;color:var(--white)}
.hero-badge{display:inline-block;border:1px solid rgba(255,255,255,.85);border-radius:14px;padding:5px 14px;font-size:11px}
.hero h1{font-size:31px;line-height:42px;font-weight:600;margin-top:16px}
.hero h1 em{font-family:var(--serif);font-style:italic;font-weight:600}
.hero p{font-size:12.5px;line-height:23px;margin-top:24px;width:440px}
.hero .btn-row{justify-content:flex-start;margin-top:28px}

/* stats */
.stats{height:204px}
.stats .container{display:grid;grid-template-columns:repeat(4,1fr);padding-top:62px}
.stat{text-align:center}
.stat strong{font-family:var(--serif);font-size:38px;font-weight:600;color:var(--blue-900);display:block;line-height:48px}
.stat span{font-size:13px;color:var(--ink)}

/* services */
.services{height:1046px;background:var(--blue-50);padding-top:70px}
.card-grid{display:grid;grid-template-columns:repeat(3,286px);gap:28px 30px;margin-top:40px}
.card{background:var(--white);border-radius:8px;height:296px;padding:30px 22px;box-shadow:0 4px 18px rgba(0,84,170,.06)}
.card .icon{width:58px;height:58px;color:var(--blue-900)}
.card h3{font-family:var(--serif);font-size:19px;font-weight:600;color:var(--navy);margin-top:26px}
.card p{font-size:12px;line-height:20.5px;color:var(--muted);margin-top:14px}
.services .btn-row{margin-top:36px}

/* why */
.why{height:879px;position:relative}
.why .head{padding-top:65px}
.why .title-line{font-size:30px;font-weight:600;line-height:42px;text-align:center}
.why .title-line em{font-family:var(--serif)}
.hub{position:absolute;left:454px;top:422px;width:292px;height:292px;border-radius:50%;border:8px solid var(--blue-200);background:linear-gradient(140deg,#dfe9f2 0%,#9fb6cb 45%,#3d5a7a 100%)}
.links{position:absolute;left:0;top:0;width:1200px;height:879px}
.point{position:absolute;width:270px}
.point .badge{width:54px;height:54px;border-radius:50%;background:var(--blue-900);border:5px solid var(--blue-200);display:flex;align-items:center;justify-content:center;color:var(--white)}
.point h4{font-family:var(--serif);font-size:15px;font-weight:600;color:var(--navy);margin-top:10px}
.point p{font-size:11.5px;line-height:16.5px;color:var(--muted);margin-top:6px}
.point.left{text-align:right}
.point.left .badge{margin-left:auto}

/* process */
.process{height:611px;background:var(--blue-50);padding-top:90px}
.process .section-title{font-family:var(--serif);font-weight:500;font-size:32px}
.process .section-lead{margin-top:18px}
.steps{position:relative;height:260px;margin-top:48px}
.step{position:absolute;width:200px;text-align:center;top:0}
.step .circle{width:100px;height:100px;border-radius:50%;background:var(--blue-900);border:6px solid var(--blue-200);margin:0 auto;position:relative;display:flex;align-items:center;justify-content:center;color:var(--white)}
.step .num{position:absolute;top:-2px;right:-6px;width:26px;height:26px;border-radius:50%;background:var(--white);color:var(--blue-900);font-size:11px;font-weight:600;display:flex;align-items:center;justify-content:center;box-shadow:0 2px 6px rgba(0,0,0,.12)}
.step h4{font-size:13.5px;font-weight:600;margin-top:12px}
.step p{font-size:11px;line-height:16px;color:var(--ink);margin-top:4px}
.process .btn-row{margin-top:-8px}

/* testimonial */
.testimonial{height:457px;padding-top:82px;text-align:center}
.quote-mark{width:62px;height:50px;margin:0 auto;color:var(--blue-400)}
blockquote{font-family:var(--serif);font-style:italic;font-size:26px;line-height:43px;color:var(--navy);width:790px;margin:24px auto 0}
.cite{font-size:13px;font-weight:500;margin-top:18px}
.creds{width:772px;margin:22px auto 0;border-top:1px solid var(--blue-200);padding-top:26px;display:flex;justify-content:center;gap:42px;font-size:14px;font-weight:500}
.creds span{display:flex;align-items:center;gap:8px}

/* cta */
.cta{height:508px}
.cta-card{position:relative;width:918px;height:396px;margin:0 auto;border-radius:60px 10px 60px 10px;overflow:hidden;background:linear-gradient(120deg,var(--blue-900) 0%,var(--blue-700) 60%)}
.cta-photo{position:absolute;right:0;top:0;width:500px;height:396px;clip-path:polygon(0 0,100% 0,100% 100%,32% 100%);background:linear-gradient(160deg,#c7d2dc 0%,#8ea4b9 45%,#4f6a86 100%)}
.cta-copy{position:absolute;left:64px;top:50px;color:var(--white);width:400px}
.cta-copy small{font-size:12px;letter-spacing:.5px}
.cta-copy h2{font-size:56px;line-height:66px;font-weight:600;margin-top:6px}
.cta-copy h2 em{font-family:var(--serif);font-style:italic;font-weight:600}
.cta-rule{width:64px;height:4px;background:var(--white);margin-top:14px}
.cta-copy p{font-size:12px;line-height:21px;margin-top:14px}
.cta-copy .btn{margin-top:22px;background:var(--white);color:var(--ink);padding:0 20px}

/* footer */
.site-footer{height:361px;background:var(--navy);color:var(--white);position:absolute;left:0;right:0;bottom:0}
.footer-grid{display:grid;grid-template-columns:312px 198px 202px 200px;padding-top:64px}
.site-footer .brand-mark{border-color:var(--white);width:46px;height:46px}
.site-footer .brand-name{color:var(--white);font-size:21px}
.site-footer .brand-tag{color:var(--white)}
.footer-about{font-size:12px;line-height:20px;margin-top:16px;width:250px}
.footer-col h5{font-size:17px;font-weight:500;margin-bottom:12px}
.footer-col li{list-style:none;font-size:12.5px;line-height:27px;display:flex;align-items:center;gap:8px}
.footer-bottom{position:absolute;left:0;right:0;bottom:0;height:44px;border-top:1px solid rgba(255,255,255,.12);text-align:center;font-size:11px;line-height:44px}
</style>
</head>
<body>

<div class="topbar">
  <div class="container">
    <span class="item phone"><svg width="12" height="12" viewBox="0 0 24 24" fill="currentColor"><path d="M6.6 10.8a15.1 15.1 0 0 0 6.6 6.6l2.2-2.2a1 1 0 0 1 1-.25 11.4 11.4 0 0 0 3.6.57 1 1 0 0 1 1 1V20a1 1 0 0 1-1 1A17 17 0 0 1 3 4a1 1 0 0 1 1-1h3.5a1 1 0 0 1 1 1c0 1.25.2 2.45.57 3.57a1 1 0 0 1-.25 1z"/></svg>CALL 123 456 7890</span>
    <span class="item"><svg width="13" height="11" viewBox="0 0 24 18" fill="currentColor"><path d="M0 0h24v18H0z" opacity=".0"/><path d="M2 0h20a2 2 0 0 1 2 2v14a2 2 0 0 1-2 2H2a2 2 0 0 1-2-2V2a2 2 0 0 1 2-2zm0 3v.5l10 6.5 10-6.5V3L12 9.2z"/></svg>hello@northvalequality.example</span>
    <div class="socials"><span></span><span></span><span></span><span></span></div>
  </div>
</div>

<header class="site-header">
  <div class="container">
    <div class="brand">
      <span class="brand-mark"></span>
      <div>
        <div class="brand-name">Northvale Consulting Group</div>
        <div class="brand-tag">FOOD SAFETY &amp; SQF CERTIFICATION</div>
      </div>
    </div>
    <nav class="nav">
      <a class="active">SERVICES</a><a>BENEFITS</a><a>PROCESS</a><a>CONTACT</a>
    </nav>
    <a class="btn btn-solid">Get SQF Consultation <span class="dot"><svg width="12" height="12" viewBox="0 0 12 12" fill="none" stroke="currentColor" stroke-width="2"><path d="M3 9l6-6M4 3h5v5"/></svg></span></a>
  </div>
</header>

<section class="hero">
  <div class="hero-photo" role="img" aria-label="Technicians in hairnets and lab coats working in a bright food production laboratory"></div>
  <div class="hero-shade"></div>
  <div class="hero-content">
    <span class="hero-badge">SQF Only · Tech Driven</span>
    <h1>Hire A Tech-driven SQF Team That Carries You Across The <em>Certification Finish Line.</em></h1>
    <p>At Northvale Consulting Group, we focus exclusively on SQF — combining real plant experience with smart technology so your team can stay focused on production while we handle the path to certification and beyond.</p>
    <div class="btn-row">
      <a class="btn btn-solid" style="background:var(--blue-900)">Get SQF Consultation <span class="dot"><svg width="12" height="12" viewBox="0 0 12 12" fill="none" stroke="currentColor" stroke-width="2"><path d="M3 9l6-6M4 3h5v5"/></svg></span></a>
      <a class="btn btn-ghost">Explore Services <span class="dot"><svg width="12" height="12" viewBox="0 0 12 12" fill="none" stroke="currentColor" stroke-width="2"><path d="M3 9l6-6M4 3h5v5"/></svg></span></a>
    </div>
  </div>
</section>

<section class="stats">
  <div class="container">
    <div class="stat"><strong>15+</strong><span>Clients Onboarded</span></div>
    <div class="stat"><strong>100%</strong><span>SQF Focused</span></div>
    <div class="stat"><strong>Digital</strong><span>Platform Built Programs</span></div>
    <div class="stat"><strong>US</strong><span>Nationwide Coverage</span></div>
  </div>
</section>

<section class="services">
  <div class="container">
    <div class="eyebrow">What We Do</div>
    <h2 class="section-title">SQF Consulting,<br>Implementation &amp; <span class="accent underline">Onboarding<svg viewBox="0 0 100 12" preserveAspectRatio="none"><path d="M2 9 Q50 2 98 6" fill="none" stroke="#0054AA" stroke-width="2"/></svg></span></h2>
    <p class="section-lead">We help food and beverage manufacturers achieve and maintain SQF certification with confidence,<br>using practical programs and digital tools that work on the floor — not just on audit day.</p>

    <div class="card-grid">
      <article class="card">
        <svg class="icon" viewBox="0 0 58 58" fill="none" stroke="currentColor" stroke-width="2"><rect x="4" y="8" width="50" height="34" rx="3"/><path d="M22 50h14M29 42v8M10 16h14v10H10zM30 16h18M30 22h12M10 32h38"/></svg>
        <h3>SQF Program Design</h3>
        <p>From sanitation program design to environmental monitoring, we help you build internal capabilities that meet USDA, FDA, and FSMA requirements and reduce dependence on external contractors.</p>
      </article>
      <article class="card">
        <svg class="icon" viewBox="0 0 58 58" fill="none" stroke="currentColor" stroke-width="2"><rect x="4" y="10" width="38" height="28" rx="3"/><rect x="36" y="6" width="16" height="44" rx="3"/><circle cx="22" cy="24" r="7"/><circle cx="22" cy="24" r="2"/><path d="M16 46h14M44 44h0"/></svg>
        <h3>Digital Platform Build</h3>
        <p>We build your SQF program directly into modern food safety software like PlantLedger or SafeBatch — digitizing forms, checklists, monitoring logs, and workflows so your team runs paperless.</p>
      </article>
      <article class="card">
        <svg class="icon" viewBox="0 0 58 58" fill="none" stroke="currentColor" stroke-width="2"><rect x="4" y="10" width="44" height="30" rx="3"/><path d="M20 48h14M26 40v8"/><circle cx="20" cy="22" r="4"/><path d="M12 34c1-5 4-7 8-7s7 2 8 7M34 6h18v12h-8l-4 4v-4h-6z"/></svg>
        <h3>Coaching &amp; Support</h3>
        <p>After building your system, we coach your team to own and maintain it day-to-day. You run the program; we provide ongoing expert guidance so you stay audit-ready at all times.</p>
      </article>
      <article class="card">
        <svg class="icon" viewBox="0 0 58 58" fill="none" stroke="currentColor" stroke-width="2"><rect x="6" y="6" width="32" height="44" rx="3"/><path d="M12 16h20M12 24h14M12 32h10"/><circle cx="38" cy="38" r="10"/><path d="M33 38l4 4 6-7"/></svg>
        <h3>Gap Assessments</h3>
        <p>We evaluate where your facility stands against SQF requirements, identify gaps, and provide a clear roadmap to close them before your audit — no surprises on certification day.</p>
      </article>
      <article class="card">
        <svg class="icon" viewBox="0 0 58 58" fill="none" stroke="currentColor" stroke-width="2"><circle cx="14" cy="14" r="6"/><circle cx="29" cy="10" r="6"/><circle cx="44" cy="14" r="6"/><path d="M4 30c2-6 6-8 10-8s8 2 10 8M19 26c2-6 6-8 10-8s8 2 10 8M34 30c2-6 6-8 10-8s8 2 10 8"/><rect x="12" y="34" width="34" height="14" rx="3"/></svg>
        <h3>Bilingual Team Support</h3>
        <p>Our team in Central America supports Spanish-speaking employees within your operation — delivering training, documentation, and coaching in the language your floor team actually speaks.</p>
      </article>
      <article class="card">
        <svg class="icon" viewBox="0 0 58 58" fill="none" stroke="currentColor" stroke-width="2"><rect x="6" y="6" width="34" height="44" rx="3"/><path d="M12 16h22M12 24h16M12 32h12"/><circle cx="40" cy="36" r="8"/><path d="M46 42l8 8"/></svg>
        <h3>Sanitation &amp; Regulatory</h3>
        <p>From sanitation program design to environmental monitoring, we help you build internal capabilities that meet USDA, FDA, and FSMA requirements and reduce dependence on external contractors.</p>
      </article>
    </div>

    <div class="btn-row">
      <a class="btn btn-solid">Get SQF Consultation <span class="dot"><svg width="12" height="12" viewBox="0 0 12 12" fill="none" stroke="currentColor" stroke-width="2"><path d="M3 9l6-6M4 3h5v5"/></svg></span></a>
      <a class="btn btn-outline">Explore Services <span class="dot"><svg width="12" height="12" viewBox="0 0 12 12" fill="none" stroke="currentColor" stroke-width="2"><path d="M3 9l6-6M4 3h5v5"/></svg></span></a>
    </div>
  </div>
</section>

<section class="why">
  <div class="head">
    <div class="eyebrow">Why Northvale Consulting</div>
    <h2 class="title-line" style="margin-top:8px">Built for Small &amp;<br>Mid-Size <span class="accent underline">Manufacturers<svg viewBox="0 0 100 12" preserveAspectRatio="none"><path d="M2 6 Q50 11 98 6" fill="none" stroke="#0054AA" stroke-width="2"/></svg></span></h2>
    <p class="section-lead" style="margin-top:24px">You don't need to hire a full-time food safety director or figure out SQF alone.<br>We bring the expertise and technology — you stay focused on production.</p>
  </div>

  <svg class="links" viewBox="0 0 1200 879" fill="none" stroke="#CADEEF" stroke-width="2">
    <path d="M406 381 H470 L520 440"/>
    <path d="M406 590 H454"/>
    <path d="M794 295 H760 L680 420"/>
    <path d="M794 486 H746"/>
    <path d="M794 672 H760 L700 660"/>
  </svg>

  <div class="hub" role="img" aria-label="Quality manager reviewing a food safety checklist on a tablet"></div>

  <div class="point left" style="left:135px;top:354px">
    <div class="badge"><svg width="22" height="22" viewBox="0 0 24 24" fill="none" stroke="currentColor" stroke-width="2"><path d="M9 3h6l-2 4h-2z"/><path d="M7 10c-2 3-3 6-3 8a3 3 0 0 0 3 3h10a3 3 0 0 0 3-3c0-2-1-5-3-8z"/><path d="M12 11v7M10 13h3a1.5 1.5 0 0 1 0 3h-2"/></svg></div>
    <h4>Lower Cost Than a Full-Time Hire</h4>
    <p>Get a complete SQF team — program design, digital implementation, and coaching — at a fraction of the cost of hiring a full-time SQF Practitioner.</p>
  </div>
  <div class="point left" style="left:135px;top:563px">
    <div class="badge"><svg width="22" height="22" viewBox="0 0 24 24" fill="none" stroke="currentColor" stroke-width="2"><circle cx="12" cy="12" r="3"/><path d="M12 2v3M12 19v3M2 12h3M19 12h3M5 5l2 2M17 17l2 2M5 19l2-2M17 7l2-2"/></svg></div>
    <h4>You Own It, We Support It</h4>
    <p>We build the system and train your team. You maintain and run it day-to-day. We stay on call with coaching and advisory so you never feel stuck.</p>
  </div>

  <div class="point" style="left:794px;top:268px">
    <div class="badge"><svg width="22" height="22" viewBox="0 0 24 24" fill="none" stroke="currentColor" stroke-width="2"><rect x="3" y="4" width="18" height="13" rx="2"/><path d="M9 21h6M12 17v4M8 9h8M8 13h5"/></svg></div>
    <h4>Your Program Lives in Software</h4>
    <p>No more binders and spreadsheets. Your SQF system is built into PlantLedger or SafeBatch — organized, accessible, and always audit-ready.</p>
  </div>
  <div class="point" style="left:794px;top:459px">
    <div class="badge"><svg width="22" height="22" viewBox="0 0 24 24" fill="none" stroke="currentColor" stroke-width="2"><path d="M12 3l7 3v5c0 5-3 8-7 10-4-2-7-5-7-10V6z"/><path d="M9 12l2 2 4-4"/></svg></div>
    <h4>Flexible, Low-Risk Engagement</h4>
    <p>Start with a 3-month commitment, then go month-to-month. Cancel anytime with 30 days notice. We earn your business every month.</p>
  </div>
  <div class="point" style="left:794px;top:645px">
    <div class="badge"><svg width="22" height="22" viewBox="0 0 24 24" fill="none" stroke="currentColor" stroke-width="2"><path d="M4 5h10v7H8l-4 3z"/><path d="M14 9h6v7l-3-2h-5v-2"/></svg></div>
    <h4>Bilingual Floor-Level Support</h4>
    <p>With our Central America team, we provide training and documentation in Spanish so every member of your production team understands and follows the program.</p>
  </div>
</section>

<section class="process">
  <div class="container">
    <div class="eyebrow">How It Works</div>
    <h2 class="section-title">From Discovery To Certification</h2>
    <p class="section-lead">A clear, structured path that takes the guesswork out of SQF.</p>

    <div class="steps">
      <svg style="position:absolute;left:0;top:0" width="920" height="100" viewBox="0 0 920 100" fill="none" stroke="#7BADD7" stroke-width="1.5" stroke-dasharray="5 5">
        <path d="M128 50 Q190 10 262 50"/>
        <path d="M372 50 Q440 90 512 50"/>
        <path d="M620 50 Q690 10 762 50"/>
      </svg>
      <div class="step" style="left:-27px">
        <div class="circle"><span class="num">01</span><svg width="40" height="40" viewBox="0 0 24 24" fill="none" stroke="currentColor" stroke-width="1.6"><path d="M5 4h3l2 5-2 1a11 11 0 0 0 6 6l1-2 5 2v3a2 2 0 0 1-2 2A16 16 0 0 1 3 6a2 2 0 0 1 2-2z"/></svg></div>
        <h4>Discovery Call</h4>
        <p>We learn about your facility, your current systems, and where you are in the SQF journey. No pressure — just a conversation.</p>
      </div>
      <div class="step" style="left:214px">
        <div class="circle"><span class="num">02</span><svg width="40" height="40" viewBox="0 0 24 24" fill="none" stroke="currentColor" stroke-width="1.6"><rect x="5" y="4" width="12" height="17" rx="1"/><path d="M9 3h4v3H9zM8 10h2M8 14h2M12 10h3M12 14h3M16 19l4-6"/></svg></div>
        <h4>Gap Assessment</h4>
        <p>We evaluate your facility against SQF requirements, identify what's missing, and give you a clear roadmap with priorities.</p>
      </div>
      <div class="step" style="left:462px">
        <div class="circle"><span class="num">03</span><svg width="40" height="40" viewBox="0 0 24 24" fill="none" stroke="currentColor" stroke-width="1.6"><path d="M9 14a5 5 0 1 1 5-2"/><path d="M8 17h3"/><circle cx="16" cy="16" r="3"/><path d="M16 11v2M16 19v2M11 16h2M19 16h2"/></svg></div>
        <h4>Build &amp; Implement</h4>
        <p>We design your SQF program and build it directly into your digital food safety platform — forms, logs, SOPs, HACCP plans, all of it.</p>
      </div>
      <div class="step" style="left:721px">
        <div class="circle"><span class="num">04</span><svg width="40" height="40" viewBox="0 0 24 24" fill="none" stroke="currentColor" stroke-width="1.6"><circle cx="12" cy="6" r="2.5"/><circle cx="5" cy="13" r="2"/><circle cx="12" cy="13" r="2"/><circle cx="19" cy="13" r="2"/><path d="M2 20c0-2 1.5-3.5 3-3.5S8 18 8 20M9 20c0-2 1.5-3.5 3-3.5s3 1.5 3 3.5M16 20c0-2 1.5-3.5 3-3.5s3 1.5 3 3.5"/></svg></div>
        <h4>Coach &amp; Certify</h4>
        <p>We train your team, run mock audits, and prepare you for certification day. Then we stay on as your ongoing SQF advisory partner.</p>
      </div>
    </div>

    <div class="btn-row">
      <a class="btn btn-solid btn-plain">Get SQF Consultation &nbsp;<svg width="20" height="12" viewBox="0 0 20 12" fill="none" stroke="currentColor" stroke-width="1.8"><path d="M1 6h17M13 1l5 5-5 5"/></svg></a>
      <a class="btn btn-outline btn-plain" style="color:var(--ink);border-color:var(--ink)">Explore Services &nbsp;<svg width="20" height="12" viewBox="0 0 20 12" fill="none" stroke="currentColor" stroke-width="1.8"><path d="M1 6h17M13 1l5 5-5 5"/></svg></a>
    </div>
  </div>
</section>

<section class="testimonial">
  <svg class="quote-mark" viewBox="0 0 62 50" fill="currentColor"><path d="M0 0h26v26c0 12-6 22-18 24l-2-7c6-2 9-6 9-11H0zM36 0h26v26c0 12-6 22-18 24l-2-7c6-2 9-6 9-11H36z"/></svg>
  <blockquote>"Northvale Consulting Group didn't just hand us a binder. They built our entire SQF system into software and coached our team until we owned it. We passed our first audit with confidence."</blockquote>
  <div class="cite">— SQF-Certified Manufacturing Client</div>
  <div class="creds">
    <span><svg width="16" height="16" viewBox="0 0 16 16"><circle cx="8" cy="8" r="8" fill="#0054AA"/><path d="M4.5 8l2.5 2.5 4.5-5" stroke="#fff" stroke-width="1.8" fill="none"/></svg>SQF Practitioner</span>
    <span><svg width="16" height="16" viewBox="0 0 16 16"><circle cx="8" cy="8" r="8" fill="#0054AA"/><path d="M4.5 8l2.5 2.5 4.5-5" stroke="#fff" stroke-width="1.8" fill="none"/></svg>Six Sigma Black Belt</span>
    <span><svg width="16" height="16" viewBox="0 0 16 16"><circle cx="8" cy="8" r="8" fill="#0054AA"/><path d="M4.5 8l2.5 2.5 4.5-5" stroke="#fff" stroke-width="1.8" fill="none"/></svg>Remote &amp; On-Site</span>
    <span><svg width="16" height="16" viewBox="0 0 16 16"><circle cx="8" cy="8" r="8" fill="#0054AA"/><path d="M4.5 8l2.5 2.5 4.5-5" stroke="#fff" stroke-width="1.8" fill="none"/></svg>Digital-First</span>
  </div>
</section>

<section class="cta">
  <div class="cta-card">
    <div class="cta-photo" role="img" aria-label="Food plant technician in hairnet and gloves checking a tablet beside stainless steel tanks"></div>
    <div class="cta-copy">
      <small>CONTACT US</small>
      <h2>Ready<br>To <em>Talk SQF?</em></h2>
      <div class="cta-rule"></div>
      <p>Share a few details about your facility and where you are in the SQF journey. We'll follow up with a brief discovery call and a clear next step.</p>
      <a class="btn">Get My SQF Consultation &nbsp;<svg width="20" height="12" viewBox="0 0 20 12" fill="none" stroke="currentColor" stroke-width="1.8"><path d="M1 6h17M13 1l5 5-5 5"/></svg></a>
    </div>
  </div>
</section>

<footer class="site-footer">
  <div class="container footer-grid">
    <div>
      <div class="brand">
        <span class="brand-mark"></span>
        <div>
          <div class="brand-name">Northvale Consulting Group</div>
          <div class="brand-tag">FOOD SAFETY &amp; SQF CERTIFICATION</div>
        </div>
      </div>
      <p class="footer-about">Tech-Driven SQF Consulting For Small And Mid-Size US Food Manufacturers. Based In Riverton, CA — Serving Clients Across North America.</p>
    </div>
    <div class="footer-col">
      <h5>Services</h5>
      <ul><li>Services</li><li>Benefits</li><li>Process</li><li>Contact</li><li>Get SQF Consultation</li></ul>
    </div>
    <div class="footer-col">
      <h5>Services</h5>
      <ul><li>SQF Program Design</li><li>Digital Platform Build</li><li>Coaching &amp; Support</li><li>Gap Assessments</li><li>Sanitation Programs</li><li>Connect</li></ul>
    </div>
    <div class="footer-col">
      <h5>Connect</h5>
      <ul>
        <li><svg width="12" height="10" viewBox="0 0 24 18" fill="#fff"><path d="M2 0h20a2 2 0 0 1 2 2v14a2 2 0 0 1-2 2H2a2 2 0 0 1-2-2V2a2 2 0 0 1 2-2zm0 3v.5l10 6.5 10-6.5V3L12 9.2z"/></svg>Email Us</li>
        <li><svg width="13" height="13" viewBox="0 0 24 24" fill="none" stroke="#fff" stroke-width="2"><circle cx="12" cy="12" r="10"/><path d="M2 12h20M12 2c3 3 3 17 0 20M12 2c-3 3-3 17 0 20"/></svg>NorthvaleQuality.example</li>
        <li><svg width="12" height="12" viewBox="0 0 12 12"><rect width="12" height="12" rx="2" fill="#fff"/></svg>ProNet</li>
      </ul>
    </div>
  </div>
  <div class="footer-bottom">© 2026 Northvale Consulting Group LLC. All Rights Reserved</div>
</footer>

</body>
</html>
```